LABEL DESIGN for our Hemp oil extract headache relief roll on

We need a pure, elegant and natural label design for our new product from Velmora CBD. We make natural and hand made products with CBD oil & other essential oils to improve wellness being. We would like to see natural, earthy and nice labels.

Target Market(s)

Gender: Feminine

Font styles to use
Serif
Sans Serif
Script

Colors
eea4c8
ffffff
b7a5cd
cadf82
7f7f7f

Requirements
Must have
• Measures of the label should be 2.35 x 2 inches.
Nice to have
• Herb leafs
Should not have
• Marijuana leafs

```html
<!DOCTYPE html>
<html lang="en">
<head>
<meta charset="utf-8">
<title>Quiet Mind – Headache Relief Roll-On Labels</title>
<link href="https://fonts.googleapis.com/css2?family=Fira+Sans+Extra+Condensed:wght@400&family=Kumbh+Sans:ital,wght@0,300;0,400;0,600;0,700;1,400&display=swap" rel="stylesheet">
<style>
  :root {
    --leaf-green: #98d96b;
    --paper: #ffffff;
    --ink: #111111;
    --cream: #ffffff;
  }
  * { margin: 0; padding: 0; box-sizing: border-box; }
  html, body { width: 1200px; height: 1200px; overflow: hidden; background: var(--paper); }
  .canvas { position: relative; width: 1200px; height: 1200px; }

  .panel { position: absolute; background: var(--leaf-green); }
  .line {
    position: absolute; left: 0; right: 0; text-align: center; white-space: nowrap;
    color: var(--ink); line-height: 1;
  }
  .condensed { font-family: "Fira Sans Extra Condensed", "Arial Narrow", sans-serif; font-weight: 400; }
  .wordmark { color: var(--cream); font-family: "Fira Sans Extra Condensed", "Arial Narrow", sans-serif; font-weight: 400; }
  .tagline { color: var(--cream); font-family: "Kumbh Sans", Arial, sans-serif; font-weight: 400; }
  .headline { font-family: "Kumbh Sans", Arial, sans-serif; font-weight: 700; }
  .subhead { font-family: "Kumbh Sans", Arial, sans-serif; font-style: italic; font-weight: 400; }
  .label-title { font-family: "Kumbh Sans", Arial, sans-serif; font-weight: 600; }
  .body-copy { font-family: "Kumbh Sans", Arial, sans-serif; font-weight: 300; letter-spacing: 0.03em; }
  .maker { font-family: "Fira Sans Extra Condensed", "Arial Narrow", sans-serif; font-weight: 400; letter-spacing: -0.01em; }

  /* Wide label */
  .wide { position: absolute; left: 50px; top: 0; width: 630px; height: 1200px; }
  .wide .front { left: 0; top: 234px; width: 630px; height: 323px; }
  .wide .back { left: 0; top: 629px; width: 630px; height: 344px; }
  .wide .intro { font-size: 18px; }
  .wide .wordmark { font-size: 96px; }
  .wide .tagline { font-size: 15px; letter-spacing: 0.33em; }
  .wide .headline { font-size: 26px; }
  .wide .subhead { font-size: 17px; }
  .wide .label-title, .wide .body-copy { font-size: 17.5px; }
  .wide .maker { font-size: 13px; }

  /* Tall label */
  .tall { position: absolute; left: 756px; top: 0; width: 399px; height: 1200px; }
  .tall .front { left: 0; top: 94px; width: 399px; height: 472px; }
  .tall .back-shape { position: absolute; left: 0; top: 622px; width: 399px; height: 491px; }
  .tall .intro { font-size: 13.5px; }
  .tall .wordmark { font-size: 78px; }
  .tall .tagline { font-size: 11.5px; letter-spacing: 0.33em; }
  .tall .headline { font-size: 20px; }
  .tall .subhead { font-size: 13px; }
  .tall .label-title, .tall .body-copy { font-size: 13px; }
  .tall .maker { font-size: 9.5px; }
</style>
</head>
<body>
<div class="canvas">

  <section class="wide">
    <div class="panel front"></div>
    <div class="panel back"></div>

    <p class="line condensed intro" style="top:302px">Natural and therapeutic balm, made with the finest and</p>
    <p class="line condensed intro" style="top:323px">purest Hemp from Colorado, known for its healing and</p>
    <p class="line condensed intro" style="top:344px">restorative properties.</p>

    <p class="line wordmark" style="top:396px">Quiet Mind</p>
    <p class="line tagline" style="top:505px">HEMP OIL EXTRACT ROLL-ON</p>

    <h1 class="line headline" style="top:572px">HEADACHE RELIEF</h1>
    <p class="line subhead" style="top:598px">Fast &amp; Natural</p>

    <p class="line label-title" style="top:679px">Direction:</p>
    <p class="line body-copy" style="top:700px">Massage into skin.</p>
    <p class="line body-copy" style="top:721px">Repeat as needed.</p>
    <p class="line label-title" style="top:764px">Ingredients:</p>
    <p class="line body-copy" style="top:785px">CBD Oil 200 mg, Rosemary,</p>
    <p class="line body-copy" style="top:806px">Mint, Beeswax, Lavender</p>

    <p class="line maker" style="top:888px">HENCHO POR VELMORA CBD</p>
    <p class="line maker" style="top:904px">ALDERBROOK, COLORADO, U.S.A.</p>
    <p class="line maker" style="top:920px">WWW.VELMORACBD.COM</p>
  </section>

  <section class="tall">
    <div class="panel front"></div>
    <svg class="back-shape" viewBox="0 0 399 491" aria-hidden="true">
      <path d="M0 0 H399 V482 Q200 498 0 482 Z" fill="var(--leaf-green)"/>
    </svg>

    <p class="line condensed intro" style="top:194px">Natural and therapeutic balm, made with the finest and</p>
    <p class="line condensed intro" style="top:210px">purest Hemp from Colorado, known for its healing and</p>
    <p class="line condensed intro" style="top:226px">restorative properties.</p>

    <p class="line wordmark" style="top:390px">Quiet Mind</p>
    <p class="line tagline" style="top:472px">HEMP OIL EXTRACT ROLL-ON</p>

    <h1 class="line headline" style="top:577px">HEADACHE RELIEF</h1>
    <p class="line subhead" style="top:598px">Fast &amp; Natural</p>

    <p class="line label-title" style="top:729px">Direction:</p>
    <p class="line body-copy" style="top:746px">Massage into skin.</p>
    <p class="line body-copy" style="top:762px">Repeat as needed.</p>
    <p class="line label-title" style="top:795px">Ingredients:</p>
    <p class="line body-copy" style="top:812px">CBD Oil 200 mg, Rosemary,</p>
    <p class="line body-copy" style="top:828px">Mint, Beeswax, Lavender</p>

    <p class="line maker" style="top:1000px">HENCHO POR VELMORA CBD</p>
    <p class="line maker" style="top:1012px">ALDERBROOK, COLORADO, U.S.A.</p>
    <p class="line maker" style="top:1025px">WWW.VELMORACBD.COM</p>
  </section>

</div>
</body>
</html>
```